Website design for an Italian restaurant in Amsterdam

I need a design for a client of mine. It is for Teatro Lunaverde, an Italian restaurant in Amsterdam.
We are going for a clean, modern look but we also need to realise an authentic feel.
The restaurant is located in an old movie theatre, that is where the name Teatro Lunaverde comes from.
Industry/Entity Type
Italian Restaurant
Number of Pages Required
1 page
Font styles to use
Sans Serif
Colors
Designer to choose colors to be used in the design.

```html
<!DOCTYPE html>
<html lang="en">
<head>
<meta charset="utf-8">
<title>Teatro Lunaverde — Italian Restaurant</title>
<link href="https://fonts.googleapis.com/css2?family=Montserrat:wght@400;500;600;700&display=swap" rel="stylesheet">
<style>
:root{
  --yellow:#f0ec1c;
  --dark:#1c1c1c;
  --darker:#151515;
  --white:#ffffff;
  --ink:#2a2a2a;
  --muted:#8a8a8a;
  --line:#cfcfcf;
  --hero-a:#2a1f3a;
  --hero-b:#5a4636;
}
*{margin:0;padding:0;box-sizing:border-box}
html,body{width:1200px;height:3303px;overflow:hidden}
body{font-family:'Montserrat',sans-serif;color:var(--ink);background:var(--white);position:relative}
.abs{position:absolute}
section,header,footer{position:absolute;left:0;width:1200px}

/* hero */
.hero{top:0;height:669px;background:radial-gradient(ellipse at 20% 40%,#6a5a54 0%,transparent 45%),radial-gradient(ellipse at 70% 75%,#4c3b2e 0%,transparent 50%),linear-gradient(160deg,var(--hero-a),#3b2c3a 45%,var(--hero-b));color:var(--white)}
.search{left:189px;top:32px;font-size:13px;letter-spacing:1px;display:flex;align-items:center;gap:12px}
.brand{left:0;width:1200px;top:28px;text-align:center;font-size:26px;font-weight:500;letter-spacing:1px}
.social{right:194px;top:34px;display:flex;gap:10px}
.social span{width:18px;height:18px;border-radius:50%;background:var(--white);display:block}
.nav{left:0;width:1200px;top:90px;display:flex;justify-content:center;gap:30px;font-size:14px}
.nav a{color:var(--white);text-decoration:none;padding-bottom:8px}
.nav a.active{color:var(--yellow);border-bottom:2px solid var(--yellow)}
.welcome{left:324px;top:240px;width:566px;height:189px;border:2px solid var(--white);text-align:center}
.welcome .kicker{margin-top:20px;font-size:17px;font-weight:500;letter-spacing:1px}
.welcome h1{font-size:38px;font-weight:600;margin-top:8px;letter-spacing:1px}
.welcome h2{font-size:25px;font-weight:600;margin-top:0}
.welcome p{font-size:13px;margin-top:8px}
.pill{height:40px;border:3px solid var(--yellow);border-radius:20px;color:var(--yellow);font-size:14px;display:flex;align-items:center;justify-content:center}
.hero .pill{left:513px;top:410px;width:176px;background:rgba(0,0,0,.25)}
.scroll{left:591px;top:588px;width:16px;height:40px;border:3px solid var(--yellow);border-radius:8px}

.title{left:0;width:1200px;text-align:center;font-size:26px;font-weight:500;letter-spacing:4px}

/* about */
.about{top:669px;height:456px}
.about .title{top:34px}
.story{top:97px;width:269px}
.story .ph{height:190px;border-radius:6px}
.story h3{font-size:13px;font-weight:600;text-align:center;margin-top:28px;letter-spacing:.5px}
.story p{font-size:12px;color:var(--muted);text-align:center;margin-top:12px;line-height:1.6;padding:0 20px}

/* menu */
.menu{top:1125px;height:394px;background:var(--dark);color:var(--white)}
.menu .title{top:34px}
.arrow{width:40px;height:20px}
.dish{top:97px;width:198px}
.dish .ph{height:198px}
.dish h4{font-size:11px;font-weight:700;margin-top:16px}
.dish p{font-size:11px;color:#7a7a7a;margin-top:6px;white-space:nowrap;overflow:hidden}

/* reservation */
.reserve{top:1519px;height:542px}
.reserve h2{left:189px;top:64px;font-size:26px;font-weight:500;letter-spacing:2px}
.field{left:189px;width:372px;border-bottom:2px solid var(--line);font-size:11px;color:#555;padding-bottom:8px}
.reserve .pill{left:189px;top:432px;width:177px;font-size:13px}
.reserve .ph{left:599px;top:62px;width:409px;height:409px;background:radial-gradient(ellipse at 50% 30%,#6b4d30,#2e2119 70%)}

/* gallery */
.gallery{top:2061px;height:394px;background:var(--dark);color:var(--white)}
.gallery .title{top:40px}
.shot{top:90px;height:304px}
.zoom{left:727px;top:220px}

/* blogs */
.blogs{top:2455px;height:579px}
.blogs .title{top:52px}
.post{top:125px;width:263px;height:326px;border:1px solid #e2e2e2;border-radius:8px;overflow:hidden;background:var(--white)}
.post .ph{height:168px}
.post .body{padding:24px 22px 0}
.post h4{font-size:15px;font-weight:700}
.post .meta{display:flex;justify-content:space-between;font-size:10px;color:#555;margin-top:14px}
.post p{font-size:11px;color:#555;margin-top:8px;line-height:1.4}
.post .more{font-size:10px;font-weight:700;color:var(--yellow);margin-top:16px}
.post .more.dark{color:var(--ink)}
.blogs .pill{left:513px;top:502px;width:176px;font-size:13px}

/* footer */
.footer{top:3034px;height:269px;background:var(--darker);color:var(--white)}
.footer .logo{left:193px;top:46px;font-size:19px;font-weight:700;color:var(--yellow);white-space:nowrap}
.footer .about-text{left:193px;top:88px;width:230px;font-size:11px;line-height:1.5}
.footer .read{left:193px;top:132px;font-size:11px;font-weight:700}
.fsocial{left:193px;top:160px;display:flex;gap:10px}
.fsocial span{width:19px;height:19px;border-radius:50%;background:var(--yellow);display:block}
.fhead{top:55px;font-size:12px;font-weight:700;color:var(--yellow)}
.flinks{left:480px;top:89px;font-size:11px;line-height:19px}
.contact{left:605px;font-size:11px;line-height:1.5;display:flex;gap:14px;align-items:flex-start}
.sub-text{left:804px;top:88px;width:220px;font-size:11px;line-height:1.5}
.email{left:804px;top:143px;width:210px;height:30px;background:var(--white);display:flex;align-items:center;font-size:10px;color:#aaa;padding-left:10px}
.send{left:968px;top:143px;width:46px;height:30px;background:var(--yellow);display:flex;align-items:center;justify-content:center}
.rule{left:193px;top:214px;width:821px;height:1px;background:#555}
.copy{left:193px;top:224px;font-size:11px}
.legal{right:186px;top:224px;font-size:11px}
</style>
</head>
<body>

<header class="hero">
  <div class="abs search">
    <svg width="18" height="18" viewBox="0 0 18 18" fill="none" stroke="#fff" stroke-width="2"><circle cx="7.5" cy="7.5" r="5.5"/><line x1="11.5" y1="11.5" x2="16" y2="16"/></svg>
    SEARCH
  </div>
  <div class="abs brand">TEATRO LUNAVERDE</div>
  <div class="abs social"><span></span><span></span><span></span><span></span></div>
  <nav class="abs nav">
    <a class="active">Home</a><a>Menu ▾</a><a>Reservation</a><a>Pages ▾</a><a>About</a><a>Contact</a>
  </nav>
  <div class="abs welcome">
    <div class="kicker">WELCOME TO</div>
    <h1>ITALIAN RESTAURANT</h1>
    <h2>TEATRO LUNAVERDE</h2>
    <p>Lorem Ipsum is simply dummy text of the printing and typesetting industry.</p>
  </div>
  <div class="abs pill">Reservation</div>
  <div class="abs scroll"></div>
</header>

<section class="about">
  <div class="abs title">About</div>
  <div class="abs story" style="left:189px">
    <div class="ph" role="img" aria-label="Restaurant dining room in warm evening light" style="background:linear-gradient(160deg,#3a3530,#1f1c1a)"></div>
    <h3>OUR RESTURENT STORY</h3>
    <p>Lorem Ipsum is simply dummy text of the printing and typesetting industry.</p>
  </div>
  <div class="abs story" style="left:465px">
    <div class="ph" role="img" aria-label="Chef plating a fresh dish" style="background:linear-gradient(160deg,#e8e2da,#9a8e80)"></div>
    <h3>ABOUT OUR MASTERCHEFS</h3>
    <p>Lorem Ipsum is simply dummy text of the printing and typesetting industry.</p>
  </div>
  <div class="abs story" style="left:740px">
    <div class="ph" role="img" aria-label="Plate of spaghetti with olive oil" style="background:linear-gradient(160deg,#6a4020,#d08a40)"></div>
    <h3>CHECK OUR MENU</h3>
    <p>Lorem Ipsum is simply dummy text of the printing and typesetting industry.</p>
  </div>
</section>

<section class="menu">
  <div class="abs title">MENU</div>
  <svg class="abs arrow" style="left:76px;top:180px" viewBox="0 0 40 20" fill="none" stroke="#fff" stroke-width="2.5"><line x1="3" y1="10" x2="38" y2="10"/><polyline points="11,2 3,10 11,18"/></svg>
  <svg class="abs arrow" style="left:1078px;top:180px" viewBox="0 0 40 20" fill="none" stroke="var(--yellow)" stroke-width="2.5"><line x1="2" y1="10" x2="37" y2="10"/><polyline points="29,2 37,10 29,18"/></svg>
  <div class="abs dish" style="left:189px"><div class="ph" role="img" aria-label="Plate of spaghetti on a dark table" style="background:radial-gradient(circle at 50% 50%,#c89a70 0%,#5a4a40 45%,#2b2b2b 75%)"></div><h4>SPEGHITY</h4><p>Lorem Ipsum is simply dummy text...</p></div>
  <div class="abs dish" style="left:396px"><div class="ph" role="img" aria-label="Plate of lasagna on a dark table" style="background:radial-gradient(circle at 50% 50%,#a87060 0%,#504440 45%,#2b2b2b 75%)"></div><h4>LASAGNA</h4><p>Lorem Ipsum is simply dummy text...</p></div>
  <div class="abs dish" style="left:603px"><div class="ph" role="img" aria-label="Whole pizza on a dark table" style="background:radial-gradient(circle at 50% 50%,#c86a3a 0%,#5a3a2a 45%,#2b2b2b 75%)"></div><h4>PIZZA</h4><p>Lorem Ipsum is simply dummy text...</p></div>
  <div class="abs dish" style="left:808px"><div class="ph" role="img" aria-label="Plate of penne pasta on a dark table" style="background:radial-gradient(circle at 50% 50%,#d0b880 0%,#5a5040 45%,#2b2b2b 75%)"></div><h4>PASTA</h4><p>Lorem Ipsum is simply dummy text...</p></div>
</section>

<section class="reserve">
  <h2 class="abs">Make Online Reservation</h2>
  <div class="abs field" style="top:118px">Full Name</div>
  <div class="abs field" style="top:166px">E-Mail</div>
  <div class="abs field" style="top:217px">Phone Number</div>
  <div class="abs field" style="top:267px">Number Of People</div>
  <div class="abs field" style="top:322px">Date Book</div>
  <div class="abs field" style="top:371px">Time</div>
  <div class="abs pill">Reservation</div>
  <div class="abs ph" role="img" aria-label="Dimly lit restaurant hall with set tables"></div>
</section>

<section class="gallery">
  <svg class="abs arrow" style="left:76px;top:36px" viewBox="0 0 40 20" fill="none" stroke="#fff" stroke-width="2.5"><line x1="3" y1="10" x2="38" y2="10"/><polyline points="11,2 3,10 11,18"/></svg>
  <div class="abs title">Gallary</div>
  <svg class="abs arrow" style="left:1078px;top:36px" viewBox="0 0 40 20" fill="none" stroke="var(--yellow)" stroke-width="2.5"><line x1="2" y1="10" x2="37" y2="10"/><polyline points="29,2 37,10 29,18"/></svg>
  <div class="abs shot" style="left:0;width:293px;background:linear-gradient(135deg,#6a8a3a,#e8e4d8 55%,#8a6a40)" role="img" aria-label="Risotto with vegetables on a checked cloth"></div>
  <div class="abs shot" style="left:293px;width:304px;background:linear-gradient(135deg,#7a4a20,#c88a48)" role="img" aria-label="Golden baked pie"></div>
  <div class="abs shot" style="left:597px;width:301px;background:linear-gradient(135deg,#2a2622,#4a3e34)" role="img" aria-label="Stuffed chicken roll, dimmed for preview"></div>
  <div class="abs shot" style="left:898px;width:302px;background:linear-gradient(135deg,#eeeae4,#d87040 60%,#f2eee8)" role="img" aria-label="Tagliatelle with tomatoes and basil"></div>
  <svg class="abs zoom" width="34" height="34" viewBox="0 0 34 34" fill="none" stroke="#fff" stroke-width="2.5"><circle cx="14" cy="14" r="11"/><line x1="22" y1="22" x2="32" y2="32"/><line x1="9" y1="14" x2="19" y2="14"/><line x1="14" y1="9" x2="14" y2="19"/></svg>
</section>

<section class="blogs">
  <div class="abs title">Latest Blogs</div>
  <article class="abs post" style="left:191px">
    <div class="ph" role="img" aria-label="Fresh salad with sauces on a wooden table" style="background:linear-gradient(135deg,#7a5030,#d0b070 50%,#6a9040)"></div>
    <div class="body"><h4>BLOG 1</h4><div class="meta"><span>▦ 19.6.2018</span><span>▭ 12 Comments</span></div><p>Lorem Ipsum is simply dummy text of the printing and typesetting industry.</p><div class="more">READ MORE...</div></div>
  </article>
  <article class="abs post" style="left:471px">
    <div class="ph" role="img" aria-label="Meatballs in tomato sauce" style="background:linear-gradient(135deg,#4a4440,#8a3a20 50%,#5a5048)"></div>
    <div class="body"><h4>BLOG 2</h4><div class="meta"><span>▦ 19.6.2018</span><span>▭ 12 Comments</span></div><p>Lorem Ipsum is simply dummy text of the printing and typesetting industry.</p><div class="more dark">READ MORE...</div></div>
  </article>
  <article class="abs post" style="left:751px">
    <div class="ph" role="img" aria-label="Table set with Italian dishes" style="background:linear-gradient(135deg,#3a3028,#c8a070 50%,#4a3a2a)"></div>
    <div class="body"><h4>BLOG 3</h4><div class="meta"><span>▦ 19.6.2018</span><span>▭ 12 Comments</span></div><p>Lorem Ipsum is simply dummy text of the printing and typesetting industry.</p><div class="more dark">READ MORE...</div></div>
  </article>
  <div class="abs pill">VIEW ALL</div>
</section>

<footer class="footer">
  <div class="abs logo">TEATRO LUNAVERDE</div>
  <div class="abs about-text">Lorem Ipsum is simply dummy text of the printing and typesetting industry.</div>
  <div class="abs read">READ MORE...</div>
  <div class="abs fsocial"><span></span><span></span><span></span><span></span></div>

  <div class="abs fhead" style="left:480px">QUICK LINK</div>
  <div class="abs flinks">Home<br>Menu<br>Reservation<br>Blogs<br>Contact</div>

  <div class="abs fhead" style="left:605px">QUICK LINK</div>
  <div class="abs contact" style="top:90px">
    <svg width="14" height="18" viewBox="0 0 14 18"><path d="M7 0a7 7 0 0 0-7 7c0 5 7 11 7 11s7-6 7-11a7 7 0 0 0-7-7z" fill="var(--yellow)"/><circle cx="7" cy="7" r="2.5" fill="#151515"/></svg>
    <span>18 Lindengracht,<br>Amsterdam 1015 KE</span>
  </div>
  <div class="abs contact" style="top:130px">
    <svg width="16" height="16" viewBox="0 0 16 16"><path d="M3 1l3 3-2 2c1 2 4 5 6 6l2-2 3 3-2 2C7 15 1 9 1 3z" fill="var(--yellow)"/></svg>
    <span>+31 20 555 0142</span>
  </div>
  <div class="abs contact" style="top:164px">
    <svg width="16" height="12" viewBox="0 0 16 12"><rect width="16" height="12" fill="var(--yellow)"/><polyline points="0,0 8,7 16,0" fill="none" stroke="#151515" stroke-width="1.5"/></svg>
    <span>hello@lunaverde-dining.nl</span>
  </div>

  <div class="abs fhead" style="left:804px">SUBSCRIBE</div>
  <div class="abs sub-text">Lorem Ipsum is simply dummy text of the printing and typesetting industry.</div>
  <div class="abs email">Email Address</div>
  <div class="abs send"><svg width="18" height="16" viewBox="0 0 18 16"><path d="M0 8L18 0 14 16 9 10z" fill="#151515"/></svg></div>

  <div class="abs rule"></div>
  <div class="abs copy">© Copyright 2018 Teatro Lunaverde - All Right Reserved</div>
  <div class="abs legal">Privacy Policy - Terms &amp; conditions</div>
</footer>

</body>
</html>
```